Build a Website for Fashion Label

Mirelle Threadworks is a fashion label, inspired by the love of fashion, colour, art, films and culture. we are looking for a web developer to help build our website. The developer requires to design and code the website to fit any device (smartphones, ovix and pc).

There are 6 pages that need to be designed:
1. New In which is home (All the images will be provided to the right candidate, but for the meantime you could use any images you got)
4. Sale
5. About Us
6. Contacts

The website will include shopping cart and:
1. Register page
2. Login
3. My Account
4. Checkout / view cart
5. Search engine

Based on the design of the website i will choose the right candidate to proceed on creating the site.

Tips on design:
Fresh design
artistic looks (French)

Hoping the business logo could give yous an idea of a fresh design, below are our Chatterly and Lumavue links:

Best Regards,
Mirelle Threadworks

```html
<!DOCTYPE html>
<html lang="en">
<head>
<meta charset="utf-8">
<title>Mirelle Threadworks — New In</title>
<link href="https://fonts.googleapis.com/css2?family=Josefin+Sans:wght@300;400;600;700&family=Montserrat:wght@400;600&family=Noto+Serif:wght@400&display=swap" rel="stylesheet">
<style>
:root{
  --ink:#1b1b1b;
  --muted:#6a6a6a;
  --faint:#a9a9a9;
  --line:#dcdcdc;
  --paper:#ffffff;
  --sale-red:#c0392b;
  --badge:#f5e44a;
  --ship-red:#c14f4c;
  --returns-blue:#4d9cc0;
  --studio:#ececec;
}
*{box-sizing:border-box;margin:0;padding:0}
html,body{width:1200px;height:2307px;overflow:hidden;background:var(--paper);color:var(--ink)}
body{position:relative;font-family:"Josefin Sans",sans-serif}
.abs{position:absolute}
.top-rule{left:53px;top:0;width:1079px;height:5px;background:var(--ink)}
.utility{left:58px;top:18px;font-family:"Noto Serif",serif;font-size:10.5px;color:var(--muted);white-space:nowrap}
.utility span{margin-right:12px}
.utility b{font-weight:400;color:var(--ink)}
.search{left:738px;top:10px;width:148px;height:27px;border:1px solid var(--line);font-family:"Noto Serif",serif;font-size:10.5px;color:var(--faint);padding:6px 10px}
.search svg{position:absolute;right:8px;top:8px}
.cart-icon{left:887px;top:10px;width:27px;height:27px;background:var(--ink)}
.cart-icon svg{position:absolute;left:6px;top:7px}
.cart-text{left:925px;top:17px;font-family:"Noto Serif",serif;font-size:10px;color:var(--muted);white-space:nowrap}
.brand{left:0;width:1200px;top:104px;text-align:center;font-family:"Josefin Sans",sans-serif;font-weight:400;font-size:28px;letter-spacing:2px;color:var(--ink)}
.brand-dot{left:595px;top:78px;width:10px;height:10px;border-radius:50%;background:var(--ink)}
.nav-line{left:53px;top:200px;width:1079px;height:1px;background:var(--line)}
.nav{left:53px;top:216px;width:1079px;display:flex;justify-content:center;gap:33px;font-family:"Montserrat",sans-serif;font-size:11.5px;letter-spacing:3px;color:#333}
.nav small{font-size:8px;letter-spacing:0}
.nav-rule{left:53px;top:246px;width:1079px;height:2px;background:var(--ink)}
.hero{left:53px;top:283px;width:1079px;height:552px;
  background:
    radial-gradient(ellipse 16% 38% at 50% 40%,rgba(176,120,96,.75),rgba(176,120,96,0) 100%),
    radial-gradient(ellipse 22% 30% at 66% 82%,rgba(150,168,128,.55),rgba(150,168,128,0) 100%),
    radial-gradient(ellipse 35% 45% at 82% 22%,rgba(226,206,200,.9),rgba(226,206,200,0) 100%),
    radial-gradient(ellipse 30% 55% at 10% 30%,rgba(40,38,18,.95),rgba(40,38,18,0) 100%),
    radial-gradient(ellipse 30% 40% at 25% 15%,rgba(150,110,40,.6),rgba(150,110,40,0) 100%),
    linear-gradient(180deg,#5d5232 0%,#8a7056 45%,#7b6048 75%,#4d3a2e 100%)}
.hero-copy{left:53px;width:1079px;text-align:center;color:#fff}
.hero-kicker{top:432px;font-family:"Montserrat",sans-serif;font-size:12px;letter-spacing:4px}
.hero-kicker-line{left:540px;top:474px;width:140px;height:1px;background:rgba(255,255,255,.7)}
.hero-title{top:486px;font-family:"Josefin Sans",sans-serif;font-weight:700;font-size:34px;letter-spacing:3px}
.hero-text{top:556px;font-family:"Noto Serif",serif;font-size:13px;line-height:19px}
.hero-btn{left:549px;top:651px;width:100px;height:36px;border:1px solid #fff;color:#fff;font-family:"Montserrat",sans-serif;font-size:10px;letter-spacing:3px;text-align:center;line-height:34px}
.arrow{width:30px;height:60px}
.tile{overflow:hidden}
.tile-label{position:absolute;left:0;width:100%;text-align:center;color:#fff}
.tile-label .k{font-family:"Montserrat",sans-serif;font-size:10.5px;letter-spacing:3px}
.tile-label .t{font-family:"Josefin Sans",sans-serif;font-weight:700;font-size:22px;letter-spacing:3px;margin-top:6px}
.promo{color:#fff}
.promo-frame{position:absolute;left:28px;top:28px;right:28px;bottom:28px;border:1px solid rgba(255,255,255,.55);text-align:center;padding-top:22px}
.promo-frame .t{font-family:"Josefin Sans",sans-serif;font-weight:700;font-size:22px;letter-spacing:3px}
.promo-frame .s{font-family:"Josefin Sans",sans-serif;font-size:13px;margin-top:10px}
.view-btn{position:absolute;left:102px;top:348px;width:142px;height:34px;border:1px solid rgba(255,255,255,.8);font-family:"Montserrat",sans-serif;font-size:10px;letter-spacing:2px;text-align:center;line-height:32px}
.tabs-line{top:1289px;height:1px;background:var(--ink)}
.tabs{left:0;width:1200px;top:1281px;text-align:center;font-family:"Josefin Sans",sans-serif;font-size:13px;color:var(--faint)}
.tabs span{background:#fff;padding:0 6px}
.tabs .on{color:var(--ink)}
.pager{left:535px;top:1311px;display:flex;gap:2px}
.pager div{width:56px;height:18px;background:var(--ink);color:#fff;font-family:"Noto Serif",serif;font-style:italic;font-size:10px;text-align:center;line-height:18px;clip-path:polygon(8% 0,92% 0,100% 50%,92% 100%,8% 100%,0 50%)}
.product-img{background:var(--studio)}
.badge{position:absolute;width:66px;height:66px;border-radius:50%;background:var(--badge);font-family:"Noto Serif",serif;font-size:11px;color:#333;text-align:center;line-height:66px}
.product-name{font-family:"Josefin Sans",sans-serif;font-size:14px;color:#333;text-align:center}
.product-price{font-family:"Josefin Sans",sans-serif;font-weight:600;font-size:14px;text-align:center}
.product-price s{color:var(--faint);font-weight:400;margin-right:6px}
.product-price .now{color:var(--sale-red)}
</style>
</head>
<body>
<div class="abs top-rule"></div>
<div class="abs utility"><span>• Wish List (0)</span><span>My Account</span><span>US Dollar ▾</span><span>English ▾</span><span>Welcome visitor you can <b>login</b> or <b>create an account</b>.</span></div>
<div class="abs search">Search<svg width="10" height="10" viewBox="0 0 10 10"><circle cx="4" cy="4" r="3" fill="none" stroke="#333" stroke-width="1.4"/><line x1="6.3" y1="6.3" x2="9.3" y2="9.3" stroke="#333" stroke-width="1.4"/></svg></div>
<div class="abs cart-icon"><svg width="15" height="13" viewBox="0 0 15 13"><path d="M0 1h3l2 7h8l2-5H4" fill="none" stroke="#fff" stroke-width="1.5"/><circle cx="6" cy="11" r="1.3" fill="#fff"/><circle cx="12" cy="11" r="1.3" fill="#fff"/></svg></div>
<div class="abs cart-text">SHOPPING CART 0 item(s) - $0.00 ▾</div>

<div class="abs brand-dot"></div>
<div class="abs brand">Mirelle Threadworks</div>

<div class="abs nav-line"></div>
<nav class="abs nav"><span>OUTERWEAR <small>▾</small></span><span>DRESSES<small>▾</small></span><span>NEW</span><span>ACCESSORIES<small>▾</small></span><span>TOPS</span><span>BOTTOMS</span><span>BAGS</span><span>SHOES</span><span>SALE</span><span>BLOG</span></nav>
<div class="abs nav-rule"></div>

<section>
  <div class="abs hero" role="img" aria-label="Woman in a floral dress riding a vintage bicycle along a misty autumn path"></div>
  <div class="abs hero-copy hero-kicker">INTRODUCING</div>
  <div class="abs hero-kicker-line"></div>
  <h1 class="abs hero-copy hero-title">AUTUMN COLLECTION 2013</h1>
  <p class="abs hero-copy hero-text">Proin gravida nibh vel velit auctor aliquet. Aenean sollicitudin, lorem quis<br>bibdum auctor, nisi elit consequat ipsum, nec sagittis sem nibh id elit. Duis sed<br>odio sit amet nibh vulputate cursus a sit amet mauris</p>
  <div class="abs hero-btn">SHOP NOW</div>
  <svg class="abs arrow" style="left:53px;top:529px" viewBox="0 0 30 60"><path d="M0 0L30 30L0 60Z" fill="#fff"/><path d="M9 24L4 30L9 36" fill="none" stroke="#555" stroke-width="1.5"/></svg>
  <svg class="abs arrow" style="left:1102px;top:529px" viewBox="0 0 30 60"><path d="M30 0L0 30L30 60Z" fill="#fff"/><path d="M21 24L26 30L21 36" fill="none" stroke="#555" stroke-width="1.5"/></svg>
</section>

<section>
  <div class="abs tile" style="left:53px;top:853px;width:347px;height:230px;background:radial-gradient(ellipse 40% 30% at 30% 75%,rgba(90,50,35,.85),rgba(90,50,35,0)),radial-gradient(ellipse 35% 30% at 85% 85%,rgba(70,45,40,.8),rgba(70,45,40,0)),radial-gradient(ellipse 30% 45% at 15% 15%,rgba(170,120,110,.8),rgba(170,120,110,0)),linear-gradient(180deg,#8e7b84 0%,#a99aa0 55%,#c5b9b8 100%)" role="img" aria-label="Legs wearing heeled shoes and sandals">
    <div class="tile-label" style="top:86px"><div class="k">THE ULTIMATE</div><div class="t">SHOES COLLECTION</div></div>
  </div>
  <div class="abs tile promo" style="left:419px;top:853px;width:348px;height:402px;background:radial-gradient(ellipse 30% 45% at 48% 42%,rgba(28,32,44,.85),rgba(28,32,44,0)),radial-gradient(ellipse 12% 25% at 50% 10%,rgba(40,110,160,.8),rgba(40,110,160,0)),linear-gradient(90deg,#4d5158 0%,#8d9699 30%,#b9c0c1 70%,#d6d9d6 100%)" role="img" aria-label="Man in a dark suit leaping in a narrow alley">
    <div class="abs" style="left:0;top:250px;width:100%;height:152px;background:linear-gradient(180deg,rgba(40,40,40,0),rgba(40,40,40,.55))"></div>
    <div class="tile-label" style="top:262px"><div class="k">SPRING 2013</div><div class="t">NEW FOR MEN</div></div>
    <div class="view-btn">VIEW COLLECTION</div>
  </div>
  <div class="abs tile" style="left:784px;top:853px;width:348px;height:230px;background:radial-gradient(ellipse 30% 35% at 62% 60%,rgba(110,85,55,.8),rgba(110,85,55,0)),radial-gradient(ellipse 30% 40% at 85% 30%,rgba(120,105,90,.8),rgba(120,105,90,0)),radial-gradient(ellipse 40% 35% at 20% 90%,rgba(70,80,40,.9),rgba(70,80,40,0)),linear-gradient(160deg,#2b2a22 0%,#4a4434 50%,#5b5340 100%)" role="img" aria-label="Woman seated on rocks holding a patterned handbag">
    <div class="tile-label" style="top:86px"><div class="k">FIND</div><div class="t">YOUR BAGS</div></div>
  </div>
  <div class="abs promo" style="left:53px;top:1099px;width:347px;height:156px;background:var(--ship-red)">
    <div class="promo-frame"><div class="t">FREE SHIPPING</div><div class="s">on order over $150.00</div></div>
  </div>
  <div class="abs promo" style="left:784px;top:1099px;width:348px;height:156px;background:var(--returns-blue)">
    <div class="promo-frame"><div class="t">FREE RETURNS</div><div class="s">free 90 days returns policy</div></div>
  </div>
</section>

<section>
  <div class="abs tabs-line" style="left:53px;width:1079px"></div>
  <div class="abs tabs"><span><span class="on">•&nbsp; LATEST</span> &nbsp;•&nbsp; BEST SELLER &nbsp;•&nbsp; SPECIAL</span></div>
  <div class="abs pager"><div>prev</div><div>next</div></div>

  <div class="abs product-img" style="left:53px;top:1345px;width:255px;height:352px;background:radial-gradient(ellipse 22% 30% at 50% 42%,rgba(80,45,38,.9),rgba(80,45,38,0)),radial-gradient(ellipse 10% 14% at 50% 82%,rgba(30,28,28,.6),rgba(30,28,28,0)),var(--studio)" role="img" aria-label="Model in a short brown dress with a handbag"><div class="badge" style="left:173px;top:18px">SALE</div></div>
  <div class="abs product-img" style="left:327px;top:1345px;width:256px;height:352px;background:radial-gradient(ellipse 22% 36% at 50% 50%,rgba(140,95,80,.85),rgba(140,95,80,0)),radial-gradient(ellipse 10% 8% at 50% 12%,rgba(150,150,160,.7),rgba(150,150,160,0)),var(--studio)" role="img" aria-label="Model in a checked coat and beret"></div>
  <div class="abs product-img" style="left:601px;top:1345px;width:256px;height:352px;background:radial-gradient(ellipse 18% 20% at 48% 38%,rgba(200,160,115,.9),rgba(200,160,115,0)),radial-gradient(ellipse 12% 26% at 50% 76%,rgba(210,30,35,.85),rgba(210,30,35,0)),var(--studio)" role="img" aria-label="Model in a camel coat and red trousers"><div class="badge" style="left:172px;top:18px">SALE</div></div>
  <div class="abs product-img" style="left:875px;top:1345px;width:257px;height:352px;background:radial-gradient(ellipse 20% 38% at 50% 52%,rgba(75,35,35,.9),rgba(75,35,35,0)),var(--studio)" role="img" aria-label="Model in a burgundy leather jacket and trousers"></div>

  <div class="abs product-name" style="left:53px;top:1719px;width:255px">Fauxwaii Shirt - Oldss</div>
  <div class="abs product-price" style="left:53px;top:1740px;width:255px"><s>$119.50</s><span class="now">$101.88</span></div>
  <div class="abs product-name" style="left:327px;top:1719px;width:256px">Framed-Sleeve Top</div>
  <div class="abs product-price" style="left:327px;top:1740px;width:256px">$83.08</div>
  <div class="abs product-name" style="left:601px;top:1719px;width:256px">Farlap Shirt - Ruby Wine</div>
  <div class="abs product-price" style="left:601px;top:1740px;width:256px"><s>$88.55</s><span class="now">$70.00</span></div>
  <div class="abs product-name" style="left:875px;top:1719px;width:257px">Crossed Shirt - Beluga</div>
  <div class="abs product-price" style="left:875px;top:1740px;width:257px">$90.13</div>

  <div class="abs product-img" style="left:53px;top:1816px;width:255px;height:365px;background:radial-gradient(ellipse 48% 70% at 50% 55%,#151515 55%,rgba(21,21,21,0) 100%),#9e9e9e" role="img" aria-label="Man in a black graphic hoodie"></div>
  <div class="abs product-img" style="left:327px;top:1816px;width:256px;height:365px;background:radial-gradient(ellipse 25% 30% at 45% 40%,rgba(200,150,90,.55),rgba(200,150,90,0)),radial-gradient(ellipse 25% 20% at 50% 100%,rgba(40,50,70,.8),rgba(40,50,70,0)),linear-gradient(180deg,#a02d39,#8a2330)" role="img" aria-label="Man in a red printed t-shirt"><div class="badge" style="left:172px;top:18px">SALE</div></div>
  <div class="abs product-img" style="left:601px;top:1816px;width:256px;height:365px;background:radial-gradient(ellipse 20% 30% at 50% 42%,rgba(30,28,28,.9),rgba(30,28,28,0)),var(--studio)" role="img" aria-label="Model in a black leather jacket and skirt"><div class="badge" style="left:172px;top:18px">SALE</div></div>
  <div class="abs product-img" style="left:875px;top:1816px;width:257px;height:365px;background:radial-gradient(ellipse 18% 38% at 50% 50%,rgba(175,135,95,.9),rgba(175,135,95,0)),var(--studio)" role="img" aria-label="Model in a tan top and trousers with a black bag"></div>

  <div class="abs product-name" style="left:53px;top:2203px;width:255px">Fauxwaii Shirt - Olds</div>
  <div class="abs product-price" style="left:53px;top:2224px;width:255px">$295.75</div>
  <div class="abs product-name" style="left:327px;top:2203px;width:256px">Framed-Sleeve Tops</div>
  <div class="abs product-price" style="left:327px;top:2224px;width:256px"><s>$106.58</s><span class="now">$107.75</span></div>
  <div class="abs product-name" style="left:601px;top:2203px;width:256px">Farlap Shirt - Ruby Wines</div>
  <div class="abs product-price" style="left:601px;top:2224px;width:256px"><s>$119.36</s><span class="now">$72.50</span></div>
  <div class="abs product-name" style="left:875px;top:2203px;width:257px">Crossed Shirt - Belugas</div>
  <div class="abs product-price" style="left:875px;top:2224px;width:257px">$120.68</div>
</section>
</body>
</html>
```